WebDesign Flyer - A5 Double Sided

We create a complete web presence for local businesses.
A comprehensive background on our services and company can be found at www.keenpixelhouse.co.uk and on the attached sales document.

We want these flyers (a5, double sided, colour) to portray us as a local, professional and friendly service that will take care fully of a business's online presence. This includes website, hosting, email, domain AND IMPORTANTLY: we also can build them a business profile on business directory websites such as NookFinder, StreetBrowse, Marbel Spots, Zorb etc. which helps them increase their profit.

Target Market(s)

Small to medium businesses found on the high street. eg: restaurants, physios, doctors, retail shops, salons, hairdressers, as well as more corporate businesses like accountancy firms and lawyers.

Industry/Entity Type

Business Directory

Requirements
Must have
• Full project files provided with all required elements if design is chosen. Design to mention: sites can be updated in less than 1 minute in 3 clicks, No contracts, money back guarantee (no risk), prices from £400, SEO as standard, keenpixelhouse.co.uk, 020 7946 0318, info@keenpixelhouse.co.uk, 10% discount with this flyer until December 20th 2010.
Nice to have
• To mention: dedicated support, business photos (see keenpixelhouse.co.uk/features), Chatterly, Quippo, ReelBox, Snapry, WorkNest Integration, free consultation, logos of services we provide (see logos.zip for examples).
Should not have
• our logo featured too prominently.

```html
<!DOCTYPE html>
<html lang="en">
<head>
<meta charset="utf-8">
<title>Keen Pixel House – A5 Flyer, Front and Back</title>
<link rel="stylesheet" href="https://fonts.googleapis.com/css2?family=Open+Sans:wght@400;700;800&family=PT+Sans:wght@400;700&display=swap">
<style>
  :root{
    --page:#ffffff;
    --chrome-top:#c9eef0;
    --chrome-bottom:#8fd8de;
    --chrome-line:#5fb8c2;
    --field:#ffffff;
    --deep:#07426f;
    --mid:#1a6fa3;
    --pale:#dff4f4;
    --mint:#bfeee6;
    --white:#ffffff;
    --yellow:#f3e94a;
    --navy:#0d3a78;
    --ink:#111111;
    --sky:#3fb6ea;
    --arrow:#2d74ad;
  }
  *{box-sizing:border-box;margin:0;padding:0}
  html,body{width:1200px;height:760px;overflow:hidden;background:var(--page)}
  body{position:relative;font-family:"PT Sans",sans-serif}

  .side-label{
    position:absolute;font-family:"Open Sans",sans-serif;font-weight:800;
    font-size:24px;color:var(--ink);transform:rotate(-90deg);transform-origin:center;
    width:120px;text-align:center;
  }
  .side-label--front{left:-42px;top:388px}
  .side-label--back{left:544px;top:388px}

  .flyer{position:absolute;top:0;width:536px;height:760px;overflow:hidden}
  .flyer--front{left:42px}
  .flyer--back{left:630px}

  .browser-bar{
    position:absolute;left:0;top:0;width:100%;height:66px;
    background:linear-gradient(var(--chrome-top),var(--chrome-bottom));
    border-bottom:1px solid var(--chrome-line);
  }
  .browser-dot{position:absolute;top:4px;width:17px;height:17px;border-radius:50%;
    background:linear-gradient(#f4ffff,#a9e3e8);border:1px solid var(--chrome-line)}
  .browser-btn{position:absolute;top:28px;height:26px;border-radius:5px;
    background:linear-gradient(#e9fbfc,#a6dfe5);border:1px solid var(--chrome-line)}
  .browser-url{
    position:absolute;left:168px;top:29px;width:310px;height:24px;background:var(--field);
    border:1px solid var(--chrome-line);border-radius:3px;font-family:"Open Sans",sans-serif;
    font-weight:700;font-size:13px;line-height:22px;padding-left:7px;color:var(--ink)
  }
  .browser-foot{position:absolute;left:0;bottom:0;width:100%;height:30px;
    background:linear-gradient(#a7e2e7,#c6eef0);border-top:1px solid var(--chrome-line)}

  .panel{position:absolute;left:0;top:66px;width:100%;height:664px}
  .flyer--front .panel{background:linear-gradient(180deg,var(--deep) 0%,var(--mid) 45%,#8fc6dc 58%,var(--pale) 66%,#eaf8f6 80%,var(--mint) 100%)}
  .flyer--back .panel{background:linear-gradient(180deg,var(--deep) 0%,#0f5a8e 35%,#2b80b0 60%,#7cc0d6 80%,var(--pale) 92%,var(--mint) 100%)}

  .deco{position:absolute;left:0;top:0}

  .price-sticker{position:absolute;left:306px;top:182px;width:166px;height:166px;border-radius:50%;
    background:radial-gradient(circle at 40% 30%,#9fe2fb,#2ba3de 70%,#1680bf);
    border:3px solid #bfeaf9;box-shadow:0 3px 8px rgba(0,0,0,.35);
    font-family:"Open Sans",sans-serif;font-weight:800;font-size:46px;color:var(--yellow);
    text-align:center;line-height:160px}

  .brand{position:absolute;left:80px;top:388px;width:400px;height:120px;display:flex;align-items:center;gap:16px}
  .brand-mark{width:58px;height:58px;border-radius:50%;background:var(--sky);flex:none}
  .brand-name{font-family:"PT Sans",sans-serif;font-weight:700;font-size:38px;color:var(--navy);line-height:1}

  .social-title{position:absolute;left:0;width:100%;top:554px;text-align:center;
    font-family:"Open Sans",sans-serif;font-weight:700;font-size:13px;color:var(--ink)}
  .social-list{position:absolute;left:142px;top:586px;display:flex;gap:18px;list-style:none}
  .social-item{width:54px;height:54px;border-radius:6px;background:#2f6fb0;
    display:flex;align-items:flex-end;justify-content:center;padding-bottom:4px;
    font-family:"PT Sans",sans-serif;font-size:10px;font-weight:700;color:var(--white)}

  .what-we-do{position:absolute;left:148px;top:89px;width:226px;height:70px;border-radius:35px;
    background:linear-gradient(#1b86cc,#0a4f95);border:5px solid #4fc6f2;
    display:flex;align-items:center;justify-content:center;gap:14px;
    font-family:"Open Sans",sans-serif;font-weight:700;font-size:21px;color:var(--white)}

  .services{position:absolute;left:97px;top:196px;font-family:"PT Sans",sans-serif;font-size:15px;line-height:18.5px}
  .service-group{margin-bottom:18px;list-style:none}
  .service-title{font-family:"Open Sans",sans-serif;font-weight:700;font-size:13.5px;color:var(--white)}
  .service-item{color:var(--yellow)}

  .contact{position:absolute;left:0;width:100%;top:598px;text-align:center;
    font-family:"Open Sans",sans-serif;font-weight:700;font-size:13.5px;line-height:18px}
  .contact-line{color:var(--navy)}
  .offer-line{color:var(--ink)}
</style>
</head>
<body>

<div class="side-label side-label--front">FRONT</div>
<div class="side-label side-label--back">BACK</div>

<section class="flyer flyer--front" aria-label="Flyer front">
  <div class="browser-bar">
    <span class="browser-dot" style="left:8px"></span>
    <span class="browser-dot" style="left:32px"></span>
    <span class="browser-dot" style="left:56px"></span>
    <span class="browser-btn" style="left:8px;width:66px"></span>
    <span class="browser-btn" style="left:88px;width:34px"></span>
    <span class="browser-btn" style="left:134px;width:34px"></span>
    <span class="browser-url">http://www.keenpixelhouse.co.uk</span>
    <span class="browser-btn" style="left:487px;width:36px"></span>
  </div>

  <div class="panel">
    <svg class="deco" width="536" height="664" viewBox="0 0 536 664" aria-hidden="true">
      <polygon class="pointer-arrow" points="-60,-18 10,-18 10,-45 60,0 10,45 10,18 -60,18"
               fill="var(--arrow)" opacity=".55" transform="translate(92 92) rotate(45) scale(1.25)"/>
      <text transform="translate(40 264) rotate(-28)" font-family="Open Sans, sans-serif" font-weight="700" font-size="21" fill="#ffffff">
        <tspan x="0" y="0">Sites can be updated in</tspan>
        <tspan x="2" dy="27">less than 1 minute in 3 clicks, SEO as standard</tspan>
        <tspan x="4" dy="27">No contracts, money back guarantee (no risk),</tspan>
        <tspan x="6" dy="27">prices from</tspan>
      </text>
    </svg>

    <div class="price-sticker">£400</div>

    <div class="brand">
      <span class="brand-mark" aria-hidden="true"></span>
      <span class="brand-name">Keen Pixel House</span>
    </div>

    <p class="social-title">Social media presence of:</p>
    <ul class="social-list">
      <li class="social-item">Chatterly</li>
      <li class="social-item">WorkNest</li>
      <li class="social-item">Quippo</li>
      <li class="social-item">ReelBox</li>
    </ul>
  </div>

  <div class="browser-foot"></div>
</section>

<section class="flyer flyer--back" aria-label="Flyer back">
  <div class="browser-bar">
    <span class="browser-dot" style="left:8px"></span>
    <span class="browser-dot" style="left:32px"></span>
    <span class="browser-dot" style="left:56px"></span>
    <span class="browser-btn" style="left:8px;width:66px"></span>
    <span class="browser-btn" style="left:88px;width:34px"></span>
    <span class="browser-btn" style="left:134px;width:34px"></span>
    <span class="browser-url">http://www.keenpixelhouse.co.uk</span>
    <span class="browser-btn" style="left:487px;width:36px"></span>
  </div>

  <div class="panel">
    <svg class="deco" width="536" height="664" viewBox="0 0 536 664" aria-hidden="true">
      <polygon points="0,330 536,60 536,250 0,520" fill="#ffffff" opacity=".06"/>
    </svg>

    <div class="what-we-do">
      <span>What We Do</span>
      <svg width="34" height="36" viewBox="0 0 34 36" aria-hidden="true">
        <polyline points="3,16 17,4 31,16" fill="none" stroke="#fff" stroke-width="6"/>
        <polyline points="3,31 17,19 31,31" fill="none" stroke="#fff" stroke-width="6"/>
      </svg>
    </div>

    <div class="services">
      <ul class="service-group">
        <li class="service-title">WEBSITE</li>
        <li class="service-item">&gt; Website</li>
        <li class="service-item">&gt; Content Management System</li>
        <li class="service-item">&gt; Professional Business Photos</li>
        <li class="service-item">&gt; Tallyview Analytics</li>
      </ul>
      <ul class="service-group">
        <li class="service-title">ONLINE PRESENCE</li>
        <li class="service-item">&gt; Search Engine Optimisation</li>
        <li class="service-item">&gt; Waymark Maps Registration</li>
        <li class="service-item">&gt; News and Blog Feed Syndication</li>
        <li class="service-item">&gt; Business Listings</li>
      </ul>
      <ul class="service-group">
        <li class="service-title">PEACE OF MIND</li>
        <li class="service-item">&gt; No Contracts</li>
        <li class="service-item">&gt;100% Satisfaction</li>
        <li class="service-item">&gt; Virus Protection</li>
        <li class="service-item">&gt;&nbsp; Technical Support</li>
      </ul>
    </div>

    <div class="contact">
      <p class="contact-line">keenpixelhouse.co.uk &nbsp;/ 020 7946 0318 / info@keenpixelhouse.co.uk</p>
      <p class="offer-line">10% discount with this flyer until December 20th 2010</p>
    </div>
  </div>

  <div class="browser-foot"></div>
</section>

</body>
</html>
```